Harborvale Ventures brochure for Investment partnership, young harold pembly

We need a brochure design to attract new investors for our investing partnership Called Harborvale Ventures. We are based in New Orleans, La. We primarily invest in stocks, bonds, and crypto but venture out into other categories as well. We would like to see designs with the black and gold like our logo. The final design should say new, fresh, sleek, tech, and honorable. BROUCHURE WILL BE 4 pages.or one folded sheet a paparer if that makes sense.
Updates

A chart showing Harborvale Ventures gains since 2019 28.6 percent and the TR 400 gAINS 7.1 PERCENT

Target Market(s)

Probable Investors

Industry/Entity Type

Financial Planning

Colors

Designer to choose only greyscale colors for use in the design.

Requirements
Must have
• Black and Gold accent. Stock market feel. Sleek, High tech, innovative, Intellgent design.
Nice to have
• Page colors possibly black.
Should not have
• Boring, Old school,

```html
<!DOCTYPE html>
<html lang="en">
<head>
<meta charset="utf-8">
<title>Harborvale Ventures – Partner Brochure</title>
<link href="https://fonts.googleapis.com/css2?family=Jost:wght@400;500;700&display=swap" rel="stylesheet">
<style>
  :root {
    --backdrop: #e8e8e6;
    --page: #050505;
    --page-fold: #121212;
    --gold: #d4b62a;
    --gold-deep: #8a7210;
    --ink: #f2f2f2;
    --ink-soft: #cfcfcf;
    --photo-light: #9a9a9a;
    --photo-dark: #2a2a2a;
  }
  * { margin: 0; padding: 0; box-sizing: border-box; }
  html, body { width: 1200px; height: 1200px; overflow: hidden; }
  body {
    background: var(--backdrop);
    font-family: "Jost", "Futura", sans-serif;
    color: var(--ink);
    position: relative;
  }
  .spread {
    position: absolute;
    width: 736px;
    height: 524px;
    background: linear-gradient(90deg, var(--page) 0%, var(--page) 46%, var(--page-fold) 50%, var(--page) 54%, var(--page) 100%);
    box-shadow: 0 2px 8px rgba(0,0,0,.25);
  }
  .spread--outer { left: 241px; top: 47px; }
  .spread--inner { left: 233px; top: 619px; }
  .abs { position: absolute; }

  .gold-tab { background: var(--gold); }
  .brand {
    color: var(--gold);
    font-weight: 500;
    text-transform: uppercase;
    letter-spacing: .08em;
    line-height: 1.1;
    text-align: center;
  }
  .brand__sub { display: block; font-size: .55em; letter-spacing: .3em; }

  .about-title { left: 47px; top: 42px; font-size: 16.5px; line-height: 20px; font-weight: 400; text-transform: uppercase; }
  .about-title strong { font-weight: 700; }
  .about-body { left: 47px; top: 86px; width: 196px; font-size: 8.4px; line-height: 10.3px; color: var(--ink-soft); }

  .gain-box { left: 36px; top: 293px; width: 168px; height: 72px; border: 1px solid var(--gold); }
  .gain-chart {
    left: 55px; top: 157px; width: 126px; height: 156px;
    background: linear-gradient(160deg, var(--gold) 0%, var(--gold-deep) 100%);
  }
  .gain-note { left: 46px; top: 329px; font-size: 8.6px; line-height: 10.6px; color: var(--ink-soft); }
  .gain-note b { color: var(--ink); font-weight: 700; }

  .footer-brand { left: 36px; top: 470px; font-size: 15px; }
  .contact { left: 164px; top: 471px; }
  .contact__title { font-size: 12px; text-transform: uppercase; }
  .contact__title strong { font-weight: 700; }
  .contact__line { margin-top: 5px; font-size: 10px; display: flex; align-items: center; gap: 3px; white-space: nowrap; }

  .cover-brand { left: 368px; width: 368px; top: 80px; font-size: 22px; }
  .cover-headline { left: 368px; width: 368px; top: 221px; text-align: center; font-size: 16.5px; line-height: 19.5px; font-weight: 400; text-transform: uppercase; }
  .cover-headline strong { color: var(--gold); font-weight: 700; }
  .cover-rule { left: 519px; top: 466px; width: 66px; height: 1px; background: #555; }
  .cover-tag { left: 368px; width: 368px; top: 478px; text-align: center; font-size: 10.5px; color: var(--ink-soft); text-transform: uppercase; }

  .intro-tab { left: 0; top: 101px; width: 20px; height: 56px; }
  .intro-text { left: 37px; top: 101px; width: 225px; font-size: 8.4px; line-height: 10.3px; color: var(--ink-soft); }
  .intro-text p + p { margin-top: 10px; }
  .frame { border: 1px solid var(--gold); }
  .frame--tram { left: 77px; top: 236px; width: 218px; height: 164px; }
  .photo { background: linear-gradient(160deg, var(--photo-light), var(--photo-dark)); }
  .photo--tram { left: 37px; top: 187px; width: 220px; height: 164px; }

  .frame--street { left: 461px; top: 17px; width: 187px; height: 122px; }
  .photo--street { left: 518px; top: 44px; width: 187px; height: 123px; }
  .how-title { left: 517px; top: 183px; font-size: 18px; font-weight: 400; text-transform: uppercase; }
  .how-title strong { font-weight: 700; }
  .how-rule { left: 517px; top: 207px; width: 56px; height: 2px; background: var(--gold); }
  .how-body { left: 517px; top: 228px; width: 188px; font-size: 8.2px; line-height: 10.3px; color: var(--ink-soft); text-align: justify; }
  .how-body p + p { margin-top: 8px; }

  .page-brand { top: 485px; font-size: 9px; }
  .page-brand--left { left: 24px; }
  .page-brand--right { left: 640px; }
  .page-tab { top: 487px; width: 11px; height: 14px; }
  .page-tab--left { left: 0; }
  .page-tab--right { left: 725px; }
</style>
</head>
<body>

<section class="spread spread--outer">
  <div class="abs gold-tab" style="left:47px;top:2px;width:20px;height:26px;"></div>
  <h2 class="abs about-title"><strong>About</strong> Harborvale Ventures<br>and General Partner</h2>
  <p class="abs about-body">Harborvale Ventures was founded in 2019 by General Partner Marcus Delaney Jr with a group economic empowerment mission. Marcus Delaney has invested int stocks since a teenager received his BA in ecomics from Bayou State College and is currently attending Gulf Coast University,</p>

  <div class="abs gain-box"></div>
  <div class="abs gain-chart" role="img" aria-label="Gold 3D bar chart illustration with a rising arrow showing growth"></div>
  <p class="abs gain-note">Harborvale Ventures<br>gains since 2019 <b>28.6 %</b><br>and the TR 400 gains <b>7.1 %</b></p>

  <div class="abs brand footer-brand">Harborvale<span class="brand__sub">Ventures</span></div>
  <div class="abs contact">
    <div class="contact__title"><strong>Contact</strong> Us</div>
    <div class="contact__line">
      <svg width="9" height="9" viewBox="0 0 10 10" aria-hidden="true"><path d="M2 1h2l1 2.5-1.3.8a5 5 0 0 0 2 2l.8-1.3L9 6v2a1 1 0 0 1-1 1A7 7 0 0 1 1 2a1 1 0 0 1 1-1z" fill="var(--ink)"/></svg>
      <span>xxx-xxxx-xx |</span>
      <svg width="9" height="9" viewBox="0 0 10 10" aria-hidden="true"><circle cx="5" cy="5" r="4" fill="none" stroke="var(--ink)"/><path d="M1 5h8M5 1c2 2 2 6 0 8M5 1c-2 2-2 6 0 8" fill="none" stroke="var(--ink)" stroke-width=".7"/></svg>
      <span>www.harborvale-example.com</span>
    </div>
  </div>

  <div class="abs brand cover-brand">Harborvale<span class="brand__sub">Ventures</span></div>
  <h1 class="abs cover-headline">Become a partner<br><strong>&amp; Build generational wealth</strong><br>by investing in the stock market</h1>
  <div class="abs cover-rule"></div>
  <p class="abs cover-tag">A first of its kind investment club</p>
</section>

<section class="spread spread--inner">
  <div class="abs gold-tab intro-tab"></div>
  <div class="abs intro-text">
    <p>If you are receiving this brochure its because someone sees you as a person that doesn't want to just work and pay bills.</p>
    <p>Your someone who wants to build real generational wealth. Not throw schemes but the using the greatest wealth builder available. The stock market.</p>
  </div>
  <div class="abs frame frame--tram"></div>
  <div class="abs photo photo--tram" role="img" aria-label="Black and white photo of a streetcar on a palm-lined city avenue"></div>

  <div class="abs frame frame--street"></div>
  <div class="abs photo photo--street" role="img" aria-label="Black and white photo of an old cathedral beside an iron-fenced alley"></div>
  <h2 class="abs how-title"><strong>How</strong> it works</h2>
  <div class="abs how-rule"></div>
  <div class="abs how-body">
    <p>Make initial deposit. The general partner will invest in stocks, bonds and other investment vehicles on your behalf.</p>
    <p>There is no upfront fees. The general partner will guarantee a 5 percent return and will work for free on your behalf until that is achieved. After the 5 percent return on the dollars invested the limited partner will receive 80 percent and the general partner will receive 20 percent of every dollar gained</p>
    <p>As the return and investments multiply the interests begins to compound annually. The legal partner legally owns shares of stock within the club and may redeem once a year or let money continue to earn interest.</p>
  </div>

  <div class="abs gold-tab page-tab page-tab--left"></div>
  <div class="abs brand page-brand page-brand--left">Harborvale<span class="brand__sub">Ventures</span></div>
  <div class="abs brand page-brand page-brand--right">Harborvale<span class="brand__sub">Ventures</span></div>
  <div class="abs gold-tab page-tab page-tab--right"></div>
</section>

</body>
</html>
```